Pinecrest Lockworks Business Card Design

Double Sided Business Card Design for a Locksmith company specializing in Safecracking, safe & vault service.

```html
<!DOCTYPE html>
<html lang="en">
<head>
<meta charset="utf-8">
<title>Pinecrest Lockworks Business Card</title>
<link rel="stylesheet" href="https://fonts.googleapis.com/css2?family=Lato:wght@400;700;900&display=swap">
<style>
  :root {
    --page: #e8e8e8;
    --card-white: #ffffff;
    --card-black: #000000;
    --brand-green: #2a7a3b;
    --ink: #222222;
    --muted: #555555;
    --rule: #6a6a6a;
    --shadow: 0 18px 40px rgba(0,0,0,0.22);
  }
  * { box-sizing: border-box; margin: 0; padding: 0; }
  html, body { width: 1200px; height: 1200px; overflow: hidden; }
  body {
    background: var(--page);
    font-family: "Lato", sans-serif;
    position: relative;
  }
  .card {
    position: absolute;
    left: 160px;
    width: 880px;
    height: 503px;
    border-radius: 26px;
    overflow: hidden;
    box-shadow: var(--shadow);
  }
  /* Front side */
  .card-front { top: 70px; background: var(--card-white); }
  .front-brand {
    position: absolute;
    left: 420px;
    top: 105px;
    display: flex;
    align-items: center;
    gap: 16px;
  }
  .brand-dot {
    width: 54px; height: 54px;
    border-radius: 50%;
    background: var(--brand-green);
    flex: none;
  }
  .front-brand .brand-name {
    font-weight: 900;
    font-size: 38px;
    line-height: 1;
    color: var(--brand-green);
    letter-spacing: 0.5px;
  }
  .divider {
    position: absolute;
    left: 330px;
    right: 40px;
    top: 256px;
    height: 1px;
    background: var(--rule);
  }
  .person {
    position: absolute;
    left: 62px;
    top: 200px;
  }
  .person-name {
    font-size: 30px;
    font-weight: 700;
    color: var(--brand-green);
    line-height: 1.1;
  }
  .person-role {
    font-size: 22px;
    color: var(--muted);
    margin-top: 4px;
  }
  .contact-list {
    position: absolute;
    left: 62px;
    top: 300px;
    list-style: none;
  }
  .contact-list li {
    display: flex;
    align-items: center;
    gap: 14px;
    font-size: 21px;
    color: var(--muted);
    line-height: 31px;
  }
  .icon { width: 16px; height: 16px; flex: none; fill: var(--brand-green); }
  .address {
    position: absolute;
    left: 590px;
    top: 282px;
    display: flex;
    gap: 12px;
    font-size: 21px;
    color: var(--muted);
    line-height: 28px;
  }
  .address .icon { margin-top: 6px; }
  .front-band {
    position: absolute;
    left: 0; bottom: 0;
    width: 100%; height: 14px;
  }
  /* Back side */
  .card-back { top: 627px; background: var(--card-black); }
  .back-brand {
    position: absolute;
    left: 0; right: 0;
    top: 160px;
    display: flex;
    justify-content: center;
    align-items: center;
    gap: 26px;
  }
  .back-brand .brand-dot { width: 120px; height: 120px; }
  .back-brand .brand-name {
    font-weight: 900;
    font-size: 64px;
    line-height: 1;
    color: var(--brand-green);
  }
  .back-url {
    position: absolute;
    left: 0; right: 0;
    top: 392px;
    text-align: center;
    font-size: 20px;
    font-weight: 700;
    letter-spacing: 5px;
    color: #ffffff;
  }
  .back-url .domain { color: var(--brand-green); font-weight: 400; }
</style>
</head>
<body>

<section class="card card-front" aria-label="Business card front">
  <div class="front-brand">
    <span class="brand-dot"></span>
    <span class="brand-name">Pinecrest Lockworks</span>
  </div>

  <div class="person">
    <p class="person-name">Marcel Hartley</p>
    <p class="person-role">Co-founder</p>
  </div>

  <div class="divider"></div>

  <ul class="contact-list">
    <li>
      <svg class="icon" viewBox="0 0 16 16" aria-hidden="true"><path d="M3.2 1.5l2.3 2.6-1.3 1.6c.9 2 2.4 3.5 4.4 4.4l1.6-1.3 2.6 2.3-1.5 2.1C6.4 12.8 3.2 9.6 1.1 4.8z"/></svg>
      +36.1.555.0148
    </li>
    <li>
      <svg class="icon" viewBox="0 0 16 16" aria-hidden="true"><path d="M2 5c0-1.5 2.7-3 6-3s6 1.5 6 3v1.5h-3V5H5v1.5H2zM3.5 8h9l1 6h-11zM8 9.5a1.8 1.8 0 100 3.6 1.8 1.8 0 000-3.6z"/></svg>
      +36.30.555.0172
    </li>
    <li>
      <svg class="icon" viewBox="0 0 16 16" aria-hidden="true"><path d="M1 3h14v10H1zM2.5 4.5L8 9l5.5-4.5z" fill-rule="evenodd"/></svg>
      pinecrestlockworks@mail.com
    </li>
    <li>
      <svg class="icon" viewBox="0 0 16 16" aria-hidden="true"><circle cx="8" cy="8" r="7"/><path d="M1 8h14M8 1c2.5 2.5 2.5 11.5 0 14M8 1c-2.5 2.5-2.5 11.5 0 14" stroke="#fff" stroke-width="1" fill="none"/></svg>
      www.pinecrestlockworks.com
    </li>
  </ul>

  <div class="address">
    <svg class="icon" viewBox="0 0 16 16" aria-hidden="true"><path d="M8 1a5 5 0 015 5c0 3.5-5 9-5 9S3 9.5 3 6a5 5 0 015-5zm0 3a2 2 0 100 4 2 2 0 000-4z" fill-rule="evenodd"/></svg>
    <p>1044 Budapest, Fenyő<br>Utca 8-12.</p>
  </div>

  <svg class="front-band" viewBox="0 0 880 14" preserveAspectRatio="none" aria-hidden="true">
    <polygon points="0,0 520,0 506,14 0,14" fill="var(--brand-green)"/>
  </svg>
</section>

<section class="card card-back" aria-label="Business card back">
  <div class="back-brand">
    <span class="brand-dot"></span>
    <span class="brand-name">Pinecrest Lockworks</span>
  </div>
  <p class="back-url">www.<span class="domain">pinecrestlockworks</span>.com</p>
</section>

</body>
</html>
```